Newsletter-Design für Online-Versandhandel
Zielgruppe
Wir sind ein online Versand Handel mit dem Schwerpunkt auf Bio Bettwaren. Unsere Zielgruppe sind ökologisch bewusste Menschen mittleren bis höheren Alters.
Aufgabenstellung
Unsere Corporate Farbe ist vornehmlich ein sanftes Grün.
www.bettwelt-lindqvar.example
Hier eine Auswahl von Newslettern
http://newsletter.waldmoos-shop.example/u/gm.php?prm=4pTrKmZyyQ_815204736_5390418_23847
http://newslink.lodenfalt.example/u/gm.php?prm=bRx72kdfQ_962157384_3047215_81530
Bisher haben wir unsere NL als kleinen, persönlichen Text gestaltet und dazu zwei oder drei Teaser.
Den Text möchte ich beibehalten und neben meiner Unterschrift ein ein kleines persönliches Bild einfügen.
Wichtig! Wir versenden mit postfink, wir benötigen eine dafür kompatible Vorlage.

```html
<!DOCTYPE html>
<html lang="de">
<head>
<meta charset="utf-8">
<title>Lindqvar Naturversand – Newsletter</title>
<link href="https://fonts.googleapis.com/css2?family=PT+Serif:wght@400;700&display=swap" rel="stylesheet">
<style>
  :root {
    --page: #ececec;
    --paper: #ffffff;
    --brand: #1f9a52;
    --card: #52ad48;
    --footer: #2db56e;
    --tag: #37b26c;
    --button: #6b6b6b;
    --ink: #2b2b2b;
    --muted: #7a7a7a;
    --title-dark: #1d3a1a;
    --rug-bg: #efefea;
    --rule: #d6d6d6;
  }
  * { box-sizing: border-box; margin: 0; padding: 0; }
  html, body { width: 1200px; height: 4000px; overflow: hidden; }
  body { background: var(--page); font-family: "PT Serif", Georgia, serif; color: var(--ink); }
  .newsletter { position: absolute; left: 121px; top: 0; width: 958px; height: 4000px; }
  .block { position: absolute; left: 0; width: 958px; }

  .topbar { top: 19px; height: 36px; background: var(--brand); color: #fff; font-size: 19px; font-weight: 700;
    display: flex; justify-content: space-between; align-items: center; padding: 0 3px 0 6px; }
  .topbar span { display: flex; align-items: center; gap: 8px; }

  .masthead { top: 55px; height: 147px; background: var(--paper); text-align: center; }
  .brand { display: inline-flex; align-items: center; gap: 14px; margin-top: 30px; }
  .brand-dot { width: 46px; height: 46px; border-radius: 50%; background: var(--brand); }
  .brand-name { font-size: 46px; color: var(--brand); font-weight: 700; }
  .brand-sub { font-size: 23px; letter-spacing: 4px; color: var(--brand); margin-top: 4px; }
  .masthead-rule { position: absolute; left: 21px; right: 21px; bottom: 0; border-top: 2px solid var(--rule); }

  .claim { top: 202px; height: 78px; background: var(--paper); text-align: center; font-size: 20px;
    letter-spacing: 1px; padding-top: 28px; }

  .hero { top: 280px; height: 416px; background: linear-gradient(100deg, #f2f3ee 0%, #ffffff 45%, #ece9e3 75%, #d8e7c4 100%); overflow: hidden; }
  .hero-badge { position: absolute; left: 76px; top: 31px; width: 171px; height: 171px; background: var(--brand);
    transform: rotate(45deg); }
  .hero-badge-text { position: absolute; left: 40px; top: 66px; width: 241px; text-align: center; color: #fff;
    font-size: 33px; line-height: 38px; }

  .welcome { top: 696px; height: 1371px; background: var(--paper); }
  .welcome h1 { position: absolute; top: 35px; width: 100%; text-align: center; font-size: 23px; font-weight: 700; }
  .welcome p { position: absolute; top: 82px; left: 10px; right: 10px; text-align: center; font-size: 17.5px;
    line-height: 34px; color: var(--muted); }
  .btn { position: absolute; left: 300px; width: 357px; height: 52px; background: var(--button); color: #fff;
    font-size: 25px; text-align: center; line-height: 52px; }

  .card { position: absolute; width: 289px; height: 443px; background: var(--card); border-radius: 8px; text-align: center; }
  .card-photo { position: absolute; left: 18px; top: 22px; width: 253px; height: 233px; }
  .card-title { position: absolute; top: 270px; width: 100%; font-size: 19px; color: var(--title-dark); }
  .card-text { position: absolute; top: 296px; left: 10px; right: 10px; font-size: 16px; line-height: 26.5px;
    color: #fff; font-weight: 700; }
  .card-price { position: absolute; top: 392px; width: 100%; font-size: 22px; color: #fff; font-weight: 700; }

  .carpets { top: 2128px; height: 332px; background: linear-gradient(180deg, #e9e3da 0%, #d9cbb7 55%, #ede8e0 100%); }
  .carpets-label { position: absolute; left: 281px; top: 134px; width: 398px; height: 62px; background: rgba(82,173,72,.85);
    color: #fff; font-size: 36px; text-align: center; line-height: 62px; }

  .rugs { top: 2460px; height: 537px; background: var(--paper); }
  .rug { position: absolute; top: 51px; width: 458px; height: 429px; background: var(--rug-bg); border: 2px solid #e2e2dc; text-align: center; }
  .rug-photo { position: absolute; left: 9px; top: 9px; width: 438px; height: 287px; }
  .rug-price { position: absolute; left: 129px; top: 296px; width: 197px; height: 66px; background: var(--tag); color: #fff;
    font-size: 26px; line-height: 66px; }
  .rug-name { position: absolute; top: 380px; width: 100%; font-size: 26px; color: var(--card); }

  .features { top: 2997px; height: 730px; background: var(--paper); }
  .feature { position: absolute; left: 84px; width: 794px; height: 330px; border: 3px solid var(--footer); }
  .feature-photo { position: absolute; left: 16px; top: 20px; width: 298px; height: 286px; }
  .feature-body { position: absolute; left: 371px; top: 30px; width: 400px; }
  .feature h2 { font-size: 26px; font-weight: 400; color: var(--card); margin-bottom: 12px; }
  .feature p { font-size: 18px; line-height: 36px; color: var(--muted); }
  .feature-price { position: absolute; left: 455px; top: 253px; width: 157px; height: 42px; background: var(--tag); color: #fff;
    font-size: 22px; text-align: center; line-height: 42px; }

  .footer { top: 3727px; height: 241px; background: var(--footer); color: #fff; }
  .footer h3 { font-size: 25px; font-weight: 400; margin-bottom: 8px; }
  .footer ul { list-style: none; font-size: 16px; font-weight: 700; line-height: 26px; }
  .footer-service { position: absolute; left: 19px; top: 14px; }
  .footer-contact { position: absolute; left: 660px; top: 14px; }
  .social { position: absolute; left: 409px; top: 176px; display: flex; gap: 17px; }
  .social span { width: 36px; height: 36px; border-radius: 6px; background: #c8242d; }
  .social span:last-child { background: #3b5998; }
</style>
</head>
<body>
<div class="newsletter">

  <div class="block topbar">
    <span>
      <svg width="18" height="14" viewBox="0 0 18 14"><rect x="0.5" y="0.5" width="17" height="13" fill="#fff"/><path d="M1 1 L9 8 L17 1" stroke="#1f9a52" stroke-width="1.6" fill="none"/></svg>
      info@bettwelt-lindqvar.example
    </span>
    <span>
      <svg width="16" height="16" viewBox="0 0 16 16"><path d="M3 1 L6 1 L7 5 L5 6.5 C6 9 7 10 9.5 11 L11 9 L15 10 L15 13 C15 14 14 15 13 15 C6 15 1 10 1 3 C1 2 2 1 3 1 Z" fill="#fff"/></svg>
      07000 555 0184
    </span>
  </div>

  <header class="block masthead">
    <div class="brand">
      <span class="brand-dot"></span>
      <span class="brand-name">Lindqvar</span>
    </div>
    <div class="brand-sub">NATURVERSAND-ONLINESHOP</div>
    <div class="masthead-rule"></div>
  </header>

  <div class="block claim">FÜR BETTWAREN, TEPPICHE UND ALLERGIEPRODUKTE</div>

  <section class="block hero" role="img" aria-label="Foto: Frau schläft entspannt in weißer Bettwäsche, grüne Blätter im Hintergrund">
    <div class="hero-badge"></div>
    <div class="hero-badge-text">Einfach<br>geschenk</div>
  </section>

  <section class="block welcome">
    <h1>Herzlich Willkommen bei Lindqvar Naturversand!</h1>
    <p>Kaufen Sie bei uns hochwertige, ökologische Produkte für natürliches Wohnen und gesundes Schlafen Handwebteppiche, Produkte zum Schutz vor Elektrosmog, orthopädische Kissen, Allergiker Bettdecken Kirschkernkissen, Nackenwärmer, Daunenkissen, Kaschmirdecken. Liegen Sie gesund und richtig in auf unseren Naturlatexmatratzen und unseren Bio Lattenrosten. Kuscheln Sie sich in unsere ökologischen Bettwaren aus kbA Baumwolle mit den verschiedensten Füllungen.</p>
    <div class="btn" style="top:274px">Weitere Informationen</div>

    <article class="card" style="left:3px;top:371px">
      <div class="card-photo" role="img" aria-label="Foto: Person liegt auf weißem Kissen" style="background:linear-gradient(180deg,#dcd6cf,#f4f4f2 60%,#7f8aa0)"></div>
      <div class="card-title">Daunen Ganzjahresdecke</div>
      <div class="card-text">Bio Ganzjahresdecke Daunen Kuschelweiche bio Daunendecke Weiße Wolke® für das ganze Jahr in organic Qualität für den</div>
      <div class="card-price">ab 359,00 € *</div>
    </article>
    <article class="card" style="left:335px;top:371px">
      <div class="card-photo" role="img" aria-label="Foto: gesteppte Bettdecke auf Holzboden" style="background:linear-gradient(160deg,#c77a2e,#efe4d0 50%,#b87431)"></div>
      <div class="card-title">Daunen Ganzjahresdecke</div>
      <div class="card-text">Bio Ganzjahresdecke Daunen Kuschelweiche bio Daunendecke Weiße Wolke® für das ganze Jahr in organic Qualität für den</div>
      <div class="card-price">ab 359,00 € *</div>
    </article>
    <article class="card" style="left:668px;top:371px">
      <div class="card-photo" role="img" aria-label="Foto: bunte Kissen und Bettwäsche im Grünen" style="background:linear-gradient(180deg,#4f7d3e,#3d6fc1 45%,#f0b52a 75%,#e0622c)"></div>
      <div class="card-title">Daunen Ganzjahresdecke</div>
      <div class="card-text">Bio Ganzjahresdecke Daunen Kuschelweiche bio Daunendecke Weiße Wolke® für das ganze Jahr in organic Qualität für den</div>
      <div class="card-price">ab 359,00 € *</div>
    </article>

    <article class="card" style="left:3px;top:837px">
      <div class="card-photo" role="img" aria-label="Foto: Kopf auf einem Nackenkissen" style="background:linear-gradient(180deg,#e4b9a4,#c98d73 50%,#efe6d6)"></div>
      <div class="card-title">Daunen Ganzjahresdecke</div>
      <div class="card-text">Bio Ganzjahresdecke Daunen Kuschelweiche bio Daunendecke Weiße Wolke® für das ganze Jahr in organic Qualität für den</div>
      <div class="card-price">ab 359,00 € *</div>
    </article>
    <article class="card" style="left:335px;top:837px">
      <div class="card-photo" role="img" aria-label="Foto: Bett mit Daunendecke vor Holzwand" style="background:linear-gradient(180deg,#8a6a4a,#c9b69a 50%,#eeeeec)"></div>
      <div class="card-title">Daunen Ganzjahresdecke</div>
      <div class="card-text">Bio Ganzjahresdecke Daunen Kuschelweiche bio Daunendecke Weiße Wolke® für das ganze Jahr in organic Qualität für den</div>
      <div class="card-price">ab 359,00 € *</div>
    </article>
    <article class="card" style="left:668px;top:837px">
      <div class="card-photo" role="img" aria-label="Foto: gestapelte Daunendecken und Kissen im Garten" style="background:linear-gradient(180deg,#3f5f2f,#f1eee5 40%,#e7e3d8)"></div>
      <div class="card-title">Daunen Ganzjahresdecke</div>
      <div class="card-text">Bio Ganzjahresdecke Daunen Kuschelweiche bio Daunendecke Weiße Wolke® für das ganze Jahr in organic Qualität für den</div>
      <div class="card-price">ab 359,00 € *</div>
    </article>

    <div class="btn" style="top:1323px">Weitere Artikel laden</div>
  </section>

  <section class="block carpets" role="img" aria-label="Foto: Wohnraum mit hellen Handwebteppichen, Sessel und Fell">
    <div class="carpets-label">Handwebteppiche</div>
  </section>

  <section class="block rugs">
    <article class="rug" style="left:3px">
      <div class="rug-photo" role="img" aria-label="Foto: blau-grauer Handwebteppich Elba" style="background:linear-gradient(180deg,#d9b43c,#9aa6ab 35%,#bcc3c4 70%,#a0612e)"></div>
      <div class="rug-price">ab 112,00 € *</div>
      <div class="rug-name">Handwebteppich Elba</div>
    </article>
    <article class="rug" style="left:497px">
      <div class="rug-photo" role="img" aria-label="Foto: orange-roter Handwebteppich Borkum" style="background:linear-gradient(180deg,#8a5a3a,#c0664a 40%,#e2873d 70%,#b5482f)"></div>
      <div class="rug-price">ab 112,00 € *</div>
      <div class="rug-name">Handwebteppich Borkum</div>
    </article>
  </section>

  <section class="block features">
    <article class="feature" style="top:0">
      <div class="feature-photo" role="img" aria-label="Foto: Nackenset mit Wärmeauflagen an Schultern und Nacken" style="background:linear-gradient(180deg,#ffffff,#b8b8b8 35%,#d66a5a 50%,#2d4a86 80%,#2db56e)"></div>
      <div class="feature-body">
        <h2>VitaWarm® Nackenset</h2>
        <p>VitaWarm® Wärmeauflagen - Nackenset Günstiges Set bei Nackenschmerzen und Verspannungen im Bereich des Nackens und der Schultern. Mit diesem Set erhalten</p>
      </div>
      <div class="feature-price">84,00 € *</div>
    </article>
    <article class="feature" style="top:359px">
      <div class="feature-photo" role="img" aria-label="Foto: Halskette mit Tigeraugen-Perlen" style="background:radial-gradient(circle at 50% 50%,#8a8f74 0%,#6b4a2c 45%,#8b9279 75%)"></div>
      <div class="feature-body">
        <h2>Tigerauge Halskette</h2>
        <p>Wunderschöne Halskette mit Edelsteinen und Silberperlen. Steine: Tigerauge, Citrin, Pyrit Silberteile, Silberverschluss Länge: ca. 45 cm auf</p>
      </div>
      <div class="feature-price">115,00 € *</div>
    </article>
  </section>

  <footer class="block footer">
    <div class="footer-service">
      <h3>SERVICE</h3>
      <ul>
        <li>Bettdecken-Ratgeber</li>
        <li>Kissen-Ratgeber</li>
        <li>Newsletter-Anmeldung</li>
        <li>Rückruf-Service</li>
      </ul>
    </div>
    <div class="footer-contact">
      <h3>KONTAKT</h3>
      <ul>
        <li>Telefonisch unter:</li>
        <li>07000 555 0184</li>
        <li>per E-Mail unter</li>
        <li>info@bettwelt-lindqvar.example</li>
      </ul>
    </div>
    <div class="social" aria-label="Soziale Netzwerke">
      <span></span><span></span><span></span>
    </div>
  </footer>

</div>
</body>
</html>
```